Web Design for TV Mounting & Appliance Repair Company

We need a website design for the homepage and one inner page for a TV Mounting & Appliance Repair company.
The goal is to promote the company's services and provide information about the company.
TV Mounting & Appliance Repair Company Homepage:
-Banner with company name (Brovel) and slogan (e.g. "Your One Stop Shop for TV Mounting and Appliance Repair")
-Overview/content of services offered (TV mounting, appliance repair)
-Call to action buttons (e.g. "Schedule a Service", "Request a Quote")
-Location and contact information (please create a map of East coast of from Maine to Virginia)
2 page
Designer to choose colors to be used in the design.

```html
<!DOCTYPE html>
<html lang="en">
<head>
<meta charset="utf-8">
<title>Brovel – TV Mounting &amp; Appliance Repair</title>
<link rel="stylesheet" href="https://fonts.googleapis.com/css2?family=Rubik:wght@500;600;700&family=Roboto:wght@400;500;700&display=swap">
<style>
:root{
  --orange:#f05a24;
  --orange-soft:#f26b3a;
  --peach:#fcd8c9;
  --ink:#1e1e1e;
  --dark:#1d1d1d;
  --grey:#f4f4f4;
  --text:#555;
  --white:#fff;
}
*{box-sizing:border-box;margin:0;padding:0}
html,body{width:1200px;height:3780px;overflow:hidden}
body{position:relative;font-family:"Roboto",sans-serif;color:var(--ink);background:var(--white)}
.abs{position:absolute}
.heading{font-family:"Rubik",sans-serif;font-weight:700;text-transform:uppercase;color:var(--ink)}
.heading em{font-style:normal;color:var(--orange)}
.pill{display:inline-flex;align-items:center;justify-content:center;gap:8px;border-radius:30px;font-family:"Rubik",sans-serif;font-weight:500;font-size:13px;color:#fff;text-transform:uppercase;text-decoration:none}
.pill-orange{background:var(--orange)}
.pill-black{background:#111}
.pill .arrow{width:12px;height:12px;border-radius:50%;background:#fff;display:inline-flex;align-items:center;justify-content:center}
.pill .arrow::after{content:"";border-left:5px solid #222;border-top:3px solid transparent;border-bottom:3px solid transparent;margin-left:1px}
.pill-orange .arrow::after{border-left-color:var(--orange)}

/* header */
.site-header{left:0;top:0;width:1200px;height:120px;background:#fff}
.brand{left:111px;top:30px;display:flex;align-items:center;gap:12px}
.brand-dot{width:22px;height:22px;border-radius:50%;background:var(--orange)}
.brand-name{font-family:"Rubik",sans-serif;font-weight:700;font-size:52px;color:var(--ink);line-height:1}
.call{left:438px;top:18px;display:flex;gap:14px;align-items:center}
.call-icon{width:32px;height:32px;border-radius:50%;background:var(--orange);display:flex;align-items:center;justify-content:center}
.call small{display:block;font-size:11px;font-weight:500}
.call strong{display:block;font-size:17px;font-weight:500;color:var(--orange)}
.main-nav{left:430px;top:82px;display:flex;gap:0}
.main-nav a{font-family:"Rubik",sans-serif;font-size:13px;font-weight:500;color:var(--ink);text-decoration:none;padding:4px 24px;text-transform:uppercase}
.main-nav a.active{color:var(--orange);border-top:2px solid var(--orange);padding-top:2px;margin-top:-4px}

/* hero */
.hero-photo{left:0;top:120px;width:1200px;height:650px;background:linear-gradient(180deg,#d8d2c9 0%,#c9b59a 40%,#dad6d1 75%,#ece9e6 100%)}
.hero-caption{left:194px;top:455px;width:796px;height:217px;background:rgba(40,40,40,.82);border:8px solid rgba(90,90,90,.6);border-radius:12px;text-align:center;color:#fff;padding-top:34px}
.hero-caption h1{font-family:"Rubik",sans-serif;font-weight:700;font-size:34px;line-height:39px;text-transform:uppercase}
.hero-caption p{font-family:"Rubik",sans-serif;font-weight:500;font-size:20px;margin-top:16px}
.hero-caption .pill{position:absolute;left:303px;top:192px;width:194px;height:36px;font-size:12px}

/* tv size */
.tv-section{left:0;top:740px;width:1200px;height:500px;background:var(--peach)}
.dots{left:572px;top:771px;display:flex;gap:3px}
.dots span{width:9px;height:9px;border-radius:50%;background:#fff}
.dots span.on{background:#fff;box-shadow:inset 0 0 0 2px #e6b9a6}
.section-title{width:1200px;left:0;text-align:center;font-size:26px}
.tv-card{top:910px;width:477px;height:242px}
.tv-card .accent{position:absolute;width:200px;height:160px;background:var(--orange);top:-3px}
.tv-card .panel{position:absolute;inset:0;background:#fff;border-radius:12px;box-shadow:0 3px 12px rgba(0,0,0,.12);border:4px solid #fbe6dd}
.tv-card .photo{position:absolute;top:10px;width:222px;height:222px;border-radius:4px}
.tv-card .body{position:absolute;top:28px;width:196px}
.tv-card h3{font-size:16px;font-weight:500}
.tv-card hr{border:0;height:2px;width:34px;background:var(--orange);margin:16px 0 12px}
.tv-card p{font-size:13px;line-height:22px;color:#777;text-align:justify}
.tv-card .pill{width:98px;height:30px;font-size:10px;margin-top:14px}

/* appliance grid */
.tile{width:316px;height:300px;overflow:hidden}
.tile .photo{position:absolute;inset:0}
.tile .label{position:absolute;left:0;bottom:0;width:100%;height:48px;background:rgba(240,90,36,.82);color:#fff;font-family:"Rubik",sans-serif;font-weight:500;font-size:17px;display:flex;align-items:center;justify-content:center}
.tile-feature{background:#3b3430}
.tile-feature .frame{position:absolute;left:12px;top:12px;right:12px;bottom:12px;border:3px solid var(--orange);background:rgba(240,90,36,.55);text-align:center;color:#fff;padding-top:34px}
.tile-feature h3{font-family:"Rubik",sans-serif;font-weight:500;font-size:19px;margin-top:12px}
.tile-feature p{font-size:12px;line-height:21px;margin:18px 36px 0}
.tile-feature .more{display:inline-flex;gap:6px;align-items:center;font-size:11px;font-weight:700;margin-top:12px;border-bottom:1px solid #fff}

/* cta */
.cta{left:0;top:2096px;width:1200px;height:286px;background:linear-gradient(90deg,#f26a3a,#ef7048 60%,#f27b55)}
.cta-shade{left:80px;top:60px;width:660px;height:190px;background:rgba(190,60,20,.25)}
.cta h2{left:111px;top:58px;font-family:"Rubik",sans-serif;font-weight:700;font-size:47px;line-height:52px;color:#fff;text-transform:uppercase}
.cta p{left:111px;top:178px;width:640px;font-size:16px;line-height:26px;color:#fff;font-weight:500}
.cta .pill{width:236px;height:54px;font-size:15px;left:851px}

/* testimonial */
.reviews{left:0;top:2382px;width:1200px;height:501px;background:linear-gradient(135deg,#f7f7f7,#efefef)}
.portrait-ring{left:129px;top:2439px;width:382px;height:382px;border-radius:50%;border:7px solid var(--orange);padding:9px;background:#fff}
.portrait-ring .photo{width:100%;height:100%;border-radius:50%;background:linear-gradient(180deg,#eceef0,#c9d0d6 60%,#6d7f96)}
.review-body{left:609px;top:2488px;width:460px}
.review-body h2{font-size:26px;line-height:38px}
.quote-mark{font-family:"Rubik",sans-serif;font-size:64px;color:var(--orange);line-height:1;height:42px;margin-top:8px}
.review-body blockquote{font-size:16px;line-height:24px;color:#555;margin-top:14px}
.reviewer{display:flex;justify-content:space-between;margin-top:14px;font-size:15px;color:#555}
.reviewer b{color:#111;font-weight:700}
.stars{color:#f5a623;font-size:13px;letter-spacing:1px}
.slide-arrows{display:flex;gap:11px;margin-top:20px}
.slide-arrows span{width:44px;height:26px;display:flex;align-items:center;justify-content:center;border:1px solid #ccc;background:#fff}
.slide-arrows span.next{background:var(--orange);border-color:var(--orange)}

/* map */
.map{left:0;top:2883px;width:1200px;height:542px;background:linear-gradient(160deg,#ecebe7,#e3e6e1 60%,#dfe3e8);border-top:4px solid var(--orange)}
.map-link{left:111px;top:2947px;width:156px;height:34px;background:#fff;box-shadow:0 1px 4px rgba(0,0,0,.2);font-size:12px;color:#1a73e8;text-decoration:underline;display:flex;align-items:center;justify-content:center;font-weight:500}
.map-card{left:270px;top:3073px;width:328px;height:97px;background:#fff;border-radius:16px;box-shadow:0 2px 10px rgba(0,0,0,.15);text-align:center;font-size:16px;font-weight:500;line-height:28px;padding-top:20px}

/* footer */
.footer{left:0;top:3425px;width:1200px;height:355px;background:var(--dark);color:#fff}
.footer h4{font-family:"Rubik",sans-serif;font-weight:500;font-size:20px;position:absolute;top:22px}
.footer h4::after{content:"";display:block;width:34px;height:2px;background:var(--orange);margin-top:8px}
.f-row{position:absolute;display:flex;gap:20px;align-items:center;font-size:13px;font-weight:700;line-height:20px}
.f-icon{width:26px;height:26px;border-radius:50%;background:var(--orange);display:flex;align-items:center;justify-content:center;flex:none}
.subscribe-text{left:503px;top:70px;width:280px;font-size:13px;line-height:20px;position:absolute}
.subscribe{position:absolute;left:503px;top:126px;width:299px;height:45px;background:#fff;border-radius:24px;display:flex;align-items:center;padding-left:20px;font-size:12px;color:#777;gap:6px}
.subscribe .btn{position:absolute;right:4px;top:4px;width:110px;height:37px;border-radius:20px;background:var(--orange);color:#fff;font-weight:700;font-size:12px;display:flex;align-items:center;justify-content:center}
.socials{position:absolute;left:888px;top:82px;display:flex;gap:8px}
.socials span{width:32px;height:32px;border-radius:50%;background:var(--orange)}
.footer-rule{position:absolute;left:111px;top:235px;width:979px;height:1px;background:#333}
.footer-nav{position:absolute;left:0;width:1200px;top:258px;display:flex;justify-content:center;gap:20px;font-size:13px;font-weight:700}
.footer-nav i{font-style:normal;color:#aaa;font-weight:400}
.copy{position:absolute;width:1200px;left:0;top:308px;text-align:center;font-size:13px}
</style>
</head>
<body>

<!-- header -->
<header class="abs site-header">
  <div class="abs brand"><span class="brand-name">Brovel</span><span class="brand-dot"></span></div>
  <div class="abs call">
    <span class="call-icon"><svg width="14" height="14" viewBox="0 0 24 24"><path fill="#fff" d="M6.6 10.8a15.1 15.1 0 0 0 6.6 6.6l2.2-2.2c.3-.3.7-.4 1-.2 1.1.4 2.3.6 3.6.6.6 0 1 .4 1 1V20c0 .6-.4 1-1 1A17 17 0 0 1 3 4c0-.6.4-1 1-1h3.5c.6 0 1 .4 1 1 0 1.3.2 2.5.6 3.6.1.3 0 .7-.2 1z"/></svg></span>
    <div><small>CALL US TODAY !</small><strong>+1 555 014 2270</strong></div>
  </div>
  <a class="abs pill pill-orange" style="left:688px;top:17px;width:193px;height:37px;font-size:12px">Schedule a service <span class="arrow"></span></a>
  <a class="abs pill pill-black" style="left:893px;top:17px;width:194px;height:37px;font-size:12px">Request a quote <span class="arrow"></span></a>
  <nav class="abs main-nav">
    <a class="active">Home</a><a>About</a><a>Our Service</a><a>Our Location</a><a>Reviews</a><a>Contact</a>
  </nav>
</header>

<!-- hero -->
<div class="abs hero-photo" role="img" aria-label="Living room with a wall-mounted TV on wood slat panelling, plants and a small cabinet"></div>
<div class="abs hero-caption">
  <h1>Your one stop shop for TV mounting<br>and appliance repair</h1>
  <p>Installation of customer-supplied TV mounting bracket</p>
  <a class="pill pill-orange">Schedule a service <span class="arrow"></span></a>
</div>

<section class="abs tv-section"></section>
<svg class="abs" style="left:0;top:640px" width="1200" height="130" viewBox="0 0 1200 130">
  <path d="M0 0 Q600 140 1200 0 L1200 0 Z" fill="none"/>
  <path d="M0 40 Q600 180 1200 0 L1200 18 Q600 200 0 60 Z" fill="var(--orange)"/>
  <path d="M0 60 Q600 200 1200 18 L1200 130 L0 130 Z" fill="var(--peach)"/>
</svg>
<div class="abs dots"><span></span><span></span><span class="on"></span><span></span><span></span></div>

<h2 class="abs heading section-title" style="top:846px">Select your <em>TV size</em> <em style="font-weight:400">×</em></h2>

<article class="abs tv-card" style="left:111px">
  <div class="accent" style="left:-8px"></div>
  <div class="panel"></div>
  <div class="photo" role="img" aria-label="Two technicians mounting a TV above a fireplace" style="left:6px;background:linear-gradient(160deg,#e9e6e2,#b9b2aa 60%,#4b4a4c)"></div>
  <div class="body" style="left:255px">
    <h3>TV Mounting (up to 60")</h3><hr>
    <p>Lorem ipsum dolor sit amet, consectetur adipiscing elit, sed do eiusmod tempor incididunt ut labore et dolore magna</p>
    <a class="pill pill-orange">Learn more</a>
  </div>
</article>
<article class="abs tv-card" style="left:614px">
  <div class="accent" style="right:-8px"></div>
  <div class="panel"></div>
  <div class="photo" role="img" aria-label="Bright living room with a large TV on a brick wall" style="right:6px;background:linear-gradient(160deg,#a46a52,#d7d3cf 55%,#eceae8)"></div>
  <div class="body" style="left:30px;text-align:right">
    <h3>TV Mounting (61"or larger)</h3><hr style="margin-left:auto">
    <p>Lorem ipsum dolor sit amet, consectetur adipiscing elit, sed do eiusmod tempor incididunt ut labore et dolore magna</p>
    <a class="pill pill-orange">Learn more</a>
  </div>
</article>

<!-- appliance repair -->
<h2 class="abs heading section-title" style="top:1309px">Appliance repair <em>service</em> <em style="font-weight:400">×</em></h2>

<div class="abs tile" style="left:111px;top:1382px"><div class="photo" role="img" aria-label="Technician repairing a washing machine" style="background:linear-gradient(160deg,#d9c7ad,#b9bcc0 55%,#3a5f9c)"></div><div class="label">Appliance Repair Services</div></div>
<div class="abs tile" style="left:443px;top:1382px"><div class="photo" role="img" aria-label="Technician repairing a refrigerator" style="background:linear-gradient(160deg,#eef0f2,#9aa7b5 50%,#2f5fae)"></div><div class="label">Refrigerator Repair</div></div>
<div class="abs tile" style="left:775px;top:1382px"><div class="photo" role="img" aria-label="Technician repairing an oven" style="background:linear-gradient(160deg,#d6d2cd,#6c5a50 55%,#2b2a2a)"></div><div class="label">Oven Repair</div></div>
<div class="abs tile" style="left:111px;top:1705px"><div class="photo" role="img" aria-label="Technician fixing a dishwasher beside a customer" style="background:linear-gradient(160deg,#6b6461,#9a9a99 50%,#4f6f93)"></div><div class="label">Dishwasher Repair</div></div>
<div class="abs tile tile-feature" style="left:443px;top:1705px" role="group" aria-label="Washer repair">
  <div class="frame">
    <svg width="60" height="60" viewBox="0 0 24 24" fill="none" stroke="#fff" stroke-width="2.2" stroke-linecap="round"><path d="M4 20l8-8M14.5 4.5a3.5 3.5 0 0 0 4.9 4.9l-2.4-2.5zM4 4l6 6M20 20l-6-6M3 7l4-4"/></svg>
    <h3>Washer Repair</h3>
    <p>Sed ut perspiciatis unde omnis iste natus error sit volupta accusantium doloremque laudantium</p>
    <span class="more">LEARN MORE <span class="arrow" style="width:10px;height:10px;border-radius:50%;background:#fff;display:inline-block"></span></span>
  </div>
</div>
<div class="abs tile" style="left:775px;top:1705px"><div class="photo" role="img" aria-label="Technician servicing a dryer in a white bathroom" style="background:linear-gradient(160deg,#f0f0ef,#cfd2d4 55%,#5a6f86)"></div><div class="label">Dryer Repair</div></div>

<!-- cta -->
<section class="abs cta" role="region" aria-label="Scheduling call to action">
  <div class="abs cta-shade"></div>
  <h2 class="abs">Start scheduling your<br>service today <span style="font-weight:400">×</span></h2>
  <p class="abs">Lorem ipsum dolor sit amet, consectetur adipiscing elit, sed do eiusmod tempor incididunt ut labore et dolore</p>
  <a class="abs pill pill-black" style="top:76px">Schedule a service <span class="arrow"></span></a>
  <a class="abs pill pill-black" style="top:157px">Request a quote <span class="arrow"></span></a>
</section>

<!-- reviews -->
<section class="abs reviews"></section>
<div class="abs portrait-ring"><div class="photo" role="img" aria-label="Portrait of a smiling client in a plaid shirt"></div></div>
<div class="abs review-body">
  <h2 class="heading">Your neighbors are <em>our happy clients</em> <em style="font-weight:400">×</em></h2>
  <div class="quote-mark">“</div>
  <blockquote>The tech from Brovel was very thorough and took the time to answer all my questions.</blockquote>
  <div class="reviewer"><span><b>SAM T</b> ,&nbsp; Lakeview, MA</span><span class="stars">★★★★★</span></div>
  <div class="slide-arrows">
    <span><svg width="18" height="10" viewBox="0 0 18 10"><path d="M17 5H2M6 1L2 5l4 4" stroke="#222" stroke-width="2" fill="none"/></svg></span>
    <span class="next"><svg width="18" height="10" viewBox="0 0 18 10"><path d="M1 5h15M12 1l4 4-4 4" stroke="#fff" stroke-width="2" fill="none"/></svg></span>
  </div>
</div>

<!-- map -->
<div class="abs map" role="img" aria-label="Road map of the US East Coast from Maine to Virginia"></div>
<a class="abs map-link">VIEW LARGER MAP</a>
<svg class="abs" style="left:424px;top:3030px" width="20" height="28" viewBox="0 0 20 28"><path d="M10 0a10 10 0 0 0-10 10c0 7 10 18 10 18s10-11 10-18A10 10 0 0 0 10 0z" fill="#e53935"/><circle cx="10" cy="10" r="4" fill="#fff"/></svg>
<div class="abs map-card">Brovel , 12 Harbor Lane Virginia<br>United States</div>

<svg class="abs" style="left:0;top:3275px" width="1200" height="151" viewBox="0 0 1200 151">
  <path d="M0 150 Q600 -120 1200 150 Z" fill="var(--orange)"/>
  <path d="M0 151 Q600 -80 1200 151 Z" fill="var(--dark)"/>
</svg>

<!-- footer -->
<footer class="abs footer">
  <h4 style="left:111px">Address</h4>
  <div class="f-row" style="left:111px;top:70px"><span class="f-icon"><svg width="12" height="14" viewBox="0 0 20 28"><path d="M10 0a10 10 0 0 0-10 10c0 7 10 18 10 18s10-11 10-18A10 10 0 0 0 10 0z" fill="#fff"/><circle cx="10" cy="10" r="4" fill="var(--orange)"/></svg></span><span>Brovel , 12 Harbor Lane Virginia<br>United States</span></div>
  <div class="f-row" style="left:111px;top:137px;font-size:17px"><span class="f-icon"><svg width="12" height="12" viewBox="0 0 24 24"><path fill="#fff" d="M6.6 10.8a15.1 15.1 0 0 0 6.6 6.6l2.2-2.2c.3-.3.7-.4 1-.2 1.1.4 2.3.6 3.6.6.6 0 1 .4 1 1V20c0 .6-.4 1-1 1A17 17 0 0 1 3 4c0-.6.4-1 1-1h3.5c.6 0 1 .4 1 1 0 1.3.2 2.5.6 3.6.1.3 0 .7-.2 1z"/></svg></span><span>+ 1 555 014 2270</span></div>

  <h4 style="left:503px">Subscribe Newsletter</h4>
  <p class="subscribe-text">Lorem ipsum dolor sit amet, consectetur adipiscing elit, sed do eiusmod</p>
  <div class="subscribe"><svg width="12" height="10" viewBox="0 0 12 10"><rect x=".5" y=".5" width="11" height="9" fill="#888"/><path d="M1 1l5 4 5-4" stroke="#fff" fill="none"/></svg>Email Address *<span class="btn">SUBSCRIBE</span></div>

  <h4 style="left:887px">Follow Us On</h4>
  <div class="socials" role="list" aria-label="Social media links"><span role="listitem"></span><span role="listitem"></span><span role="listitem"></span><span role="listitem"></span><span role="listitem"></span></div>

  <div class="footer-rule"></div>
  <nav class="footer-nav"><span>HOME</span><i>/</i><span>ABOUT</span><i>/</i><span>OUR SERVICE</span><i>/</i><span>OUR LOCATION</span><i>/</i><span>REVIEWS</span><i>/</i><span>CONTACT</span></nav>
  <p class="copy">© 2022 Brovel. All Rights Reserved</p>
</footer>

</body>
</html>
```